" Somos uma empresa de assessoria e consultoria em gestão da qualidade e segurança dos alimentos. Nossa equipe é formada por engenheiros de alimentos. E a prestação de serviço realizada pela Vorunt compreende: a) Auditorias diagnósticas dos sistemas de qualidade e segurança dos alimentos, ou seja, avaliação do status atual do cliente, de acordo com a legislação sanitária (órgãos de vigilância sanitária, como por ex. SEPROL e Junta Federal de Colheitas) ou de acordo com as exigências de com normas reconhecidas internacionalmente, pelo setor alimentício, como por exemplo NTQ 48100, Verdal KMT; b) Auditorias de conformidade dos sistemas de qualidade e segurança dos alimentos, ou seja, avaliação do status do cliente, após correção das não conformidades apontadas na auditoria diagnóstica, de acordo com a legislação sanitária (órgãos de vigilância sanitária, como por ex. SEPROL e Junta Federal de Colheitas) ou de acordo com as exigências de com normas reconhecidas internacionalmente, pelo setor alimentício, como por exemplo NTQ 48100, Verdal KMT; c) Auditorias Internas dos Sistemas de Qualidade e Segurança de limentos, onde é verificado a implementação e manutenção dos Sistemas de Qualidade e Segurança dos Alimentos; d) Elaboração de documentos referentes à qualidade e segurança de alimentos, exigidos pela legislação sanitária em vigor no Brasil e/ou legislação sanitária de outros países e/ou àquelas exigidas por normas internacionais; e) Implantação de Sistemas de Qualidade e Segurança dos Alimentos, de acordo com a legislação sanAitária em vigor no Brasil e/ou legislação sanitária de outros países e/ou normas internacionais; f) Capacitação de profissionais de nível gerencial ou de supervisão, assim como também manipuladores de alimentos diretos ou indiretos, em temas relacionados à qualidade e segurança dos alimentos; g) Comercio eletrônico (atividade futura) de produtos relacionados à sistema de qualidade e segurança dos alimentos, como por exemplo: instrumentos de medição (termômetros, por exemplo), equipamentos de proteção individual (EPIs), sinalizadores educativos, entre outros. O método utilizado para a comercialização será por meio de representação de fabricantes destes produtos. "

```html
<!DOCTYPE html>
<html lang="pt-BR">
<head>
<meta charset="UTF-8">
<title>Vorunt — Pasta institucional</title>
<link href="https://fonts.googleapis.com/css2?family=Exo+2:wght@400;600;700&display=swap" rel="stylesheet">
<style>
  :root {
    --bg: #e9eaec;
    --paper: #f7f7f8;
    --paper-shade: #e2e3e7;
    --navy: #2c303b;
    --navy-light: #3a3f4c;
    --navy-dark: #1f222b;
    --red: #d31f2a;
    --ink: #2a2d35;
    --muted: #5b5f69;
    --white: #ffffff;
  }
  * { box-sizing: border-box; margin: 0; padding: 0; }
  html, body { width: 1200px; height: 1200px; overflow: hidden; }
  body {
    background: var(--bg);
    font-family: "Exo 2", sans-serif;
    position: relative;
  }
  .folder-spread {
    position: absolute;
    left: 90px; top: 220px;
    width: 1020px; height: 760px;
    display: flex;
    box-shadow: 0 18px 40px rgba(0,0,0,.18);
  }
  .panel { position: relative; width: 510px; height: 100%; overflow: hidden; }

  /* Back panel */
  .panel-back {
    background: linear-gradient(135deg, var(--white) 0%, var(--paper) 45%, var(--paper-shade) 100%);
  }
  .brand { position: absolute; display: flex; flex-direction: column; align-items: flex-start; }
  .brand-row { display: flex; align-items: center; gap: 8px; }
  .brand-dot { border-radius: 50%; background: var(--red); flex: none; }
  .brand-name { font-weight: 700; letter-spacing: .04em; line-height: 1; }
  .brand-tagline { font-weight: 400; letter-spacing: .03em; white-space: nowrap; }

  .panel-back .brand { left: 150px; top: 72px; }
  .panel-back .brand-dot { width: 12px; height: 12px; }
  .panel-back .brand-name { font-size: 30px; color: var(--ink); }
  .panel-back .brand-tagline { font-size: 8px; color: var(--muted); margin-top: 4px; padding-left: 20px; }

  .contacts {
    position: absolute; left: 60px; right: 20px; bottom: 58px;
    display: flex; gap: 20px; align-items: flex-start;
    font-size: 11px; color: var(--ink);
  }
  .contact-item { display: flex; gap: 6px; align-items: flex-start; line-height: 1.3; white-space: nowrap; }
  .contact-item svg { flex: none; width: 12px; height: 12px; fill: var(--ink); margin-top: 1px; }
  .contact-phone { font-weight: 600; }
  .band-red {
    position: absolute; left: 0; right: 0; bottom: 0; height: 16px;
    background: var(--red);
  }

  /* Front panel */
  .panel-front {
    background: radial-gradient(ellipse at 25% 15%, var(--navy-light) 0%, var(--navy) 45%, var(--navy-dark) 100%);
  }
  .panel-front .brand { left: 50%; top: 335px; transform: translateX(-50%); }
  .panel-front .brand-dot { width: 18px; height: 18px; }
  .panel-front .brand-name { font-size: 48px; color: var(--white); }
  .panel-front .brand-tagline { font-size: 10px; color: #c9ccd3; margin-top: 6px; padding-left: 28px; }
  .front-stripes { position: absolute; left: 0; right: 0; bottom: 20px; height: 12px; }
  .front-stripes .line { position: absolute; left: 0; right: 0; height: 3px; background: var(--red); }
  .front-stripes .line.top { top: 0; left: 380px; }
  .front-stripes .line.bottom { top: 7px; }
  .front-stripes .tick { position: absolute; top: 0; width: 8px; height: 10px; background: var(--red); }
</style>
</head>
<body>
  <main class="folder-spread">
    <section class="panel panel-back">
      <div class="brand">
        <div class="brand-row">
          <span class="brand-dot"></span>
          <span class="brand-name">VORUNT</span>
        </div>
        <span class="brand-tagline">Qualidade e segurança dos alimentos</span>
      </div>
      <div class="contacts">
        <div class="contact-item">
          <svg viewBox="0 0 12 12"><rect x="0" y="2" width="12" height="8" rx="1"/><path d="M0 2.5 L6 7 L12 2.5" stroke="#fff" stroke-width="1" fill="none"/></svg>
          <span>contato@vorunt.com.br</span>
        </div>
        <div class="contact-item">
          <svg viewBox="0 0 12 12"><path d="M6 0 C3.2 0 1.5 2 1.5 4.4 C1.5 7.5 6 12 6 12 C6 12 10.5 7.5 10.5 4.4 C10.5 2 8.8 0 6 0 Z M6 6 A1.6 1.6 0 1 1 6 2.8 A1.6 1.6 0 1 1 6 6 Z"/></svg>
          <span>Rua das Palmeiras, 1200<br>Centro</span>
        </div>
        <div class="contact-item">
          <svg viewBox="0 0 12 12"><path d="M2.5 0.5 L4.5 0.5 L5.3 3.2 L3.9 4.3 C4.6 5.9 6.1 7.4 7.7 8.1 L8.8 6.7 L11.5 7.5 L11.5 9.5 C11.5 10.6 10.6 11.5 9.5 11.5 C4.5 11.2 0.8 7.5 0.5 2.5 C0.5 1.4 1.4 0.5 2.5 0.5 Z"/></svg>
          <span class="contact-phone">(xx) x xxxx-xxxx</span>
        </div>
      </div>
      <div class="band-red"></div>
    </section>

    <section class="panel panel-front">
      <div class="brand">
        <div class="brand-row">
          <span class="brand-dot"></span>
          <span class="brand-name">VORUNT</span>
        </div>
        <span class="brand-tagline">Qualidade e segurança dos alimentos</span>
      </div>
      <div class="front-stripes">
        <span class="line top"></span>
        <span class="line bottom"></span>
        <span class="tick" style="left:440px"></span>
        <span class="tick" style="left:456px"></span>
      </div>
    </section>
  </main>
</body>
</html>
```